In-Design Template: Single-sided A3 Brochure

Hi In-Design Experts,

I am after an A3 template which is created using In-Design. It needs to be able to operate in CS3.

This template will be used as the basis for a brochure for a beautiful range of stationery. In order to help me with the layout of the brochure, I require a template to be created using "In-Design". The template that you will create will include Rectangle Frames that will allow me to easily insert my products.

As this template is hard to describe in words, I have attached a diagram of what I am actually after. This is an A3 brochure (created on a slightly bigger canvas). As you will see, the right side is an exact replica of the left side. In creating the brochure, think of beautiful shades of pinks - incorporating baby pinks and pastel pinks - elegant, classy and beautiful.

Further details provided below and in the attached files.

If you require any further information or have any questions, please let me know.

Looking forward to seeing your designs.

Target Market(s)

Women

Requirements
Must have
• Template must be created using "In-Design" and be able to operate in version CS3.
• Template information - In the supporting files, I have set out the following:
• - Size of template (Image A3 created on canvas size SRA3 (450 x 320mm) with crop marks
• - Location of all text areas
• - Location of the boxes for my products - Please use the "Rectangle Frame Tool" to allow me to insert products later on.
• Further Design Work - The template is the basis and I would then require your creativity for the following design work:
• - Text to be included at the top of each page - "Vitrel" using Edwarian Script (or similar font style. Please use the pink tones described above.
• - Image - I have attached an image that I would like to include in some way. I am thinking of placing this in the corners of the brochure - but opened to ideas. The image is a picture of scattered leaves. The picture I have attached is in shades of purple, however, I would require the leaves in shades of Pink. I am open to how you use these leaves in the template/brochure. You definitely do not need to use the exact leaves as displayed but something similar would be perfect.

```html
<!DOCTYPE html>
<html lang="en">
<head>
<meta charset="utf-8">
<title>Vitrel – Stationery Brochure Template</title>
<link rel="stylesheet" href="https://fonts.googleapis.com/css2?family=Great+Vibes&family=Tinos&display=swap">
<style>
  :root {
    --bleed-pink: #f8dada;
    --page-white: #ffffff;
    --script-pink: #eea3a9;
    --leaf-deep: #e07a90;
    --leaf-mid: #eba3b3;
    --leaf-pale: #f3d3dc;
    --ink: #3b3b3b;
    --frame-grey: #8a8a8a;
    --crop-black: #111111;
  }
  * { margin: 0; padding: 0; box-sizing: border-box; }
  html, body { width: 1200px; height: 880px; overflow: hidden; }
  body { background: var(--bleed-pink); font-family: "Tinos", "Times New Roman", serif; }
  .canvas { position: relative; width: 1200px; height: 880px; background: var(--bleed-pink); }
  .crop-marks { position: absolute; inset: 0; }
  .page { position: absolute; left: 46px; top: 51px; width: 1107px; height: 777px; background: var(--page-white); overflow: hidden; }
  .leaves-top {
    position: absolute; left: 0; top: 0; width: 100%; height: 60px;
    background: linear-gradient(180deg, var(--leaf-mid) 0%, var(--leaf-pale) 45%, rgba(255,255,255,0) 100%);
    opacity: .85;
  }
  .leaves-bottom {
    position: absolute; bottom: 0; height: 26px;
    background: linear-gradient(0deg, var(--leaf-mid) 0%, var(--leaf-pale) 50%, rgba(255,255,255,0) 100%);
    opacity: .8;
  }
  .leaves-bottom.left { left: 0; width: 110px; }
  .leaves-bottom.centre { left: 390px; width: 330px; }
  .leaves-bottom.right { right: 0; width: 110px; }
  .spread-half { position: absolute; top: 0; width: 554px; height: 777px; }
  .spread-half.left { left: 0; }
  .spread-half.right { left: 558px; }
  .brand-title {
    position: absolute; top: 22px; left: 0; width: 100%; text-align: center;
    font-family: "Great Vibes", cursive; font-weight: 400; font-size: 56px; line-height: 1;
    color: var(--script-pink);
  }
  .section-heading {
    position: absolute; top: 79px; left: 0; width: 100%; text-align: center;
    font-size: 20px; font-weight: 400; line-height: 1; color: var(--ink);
  }
  .website {
    position: absolute; top: 753px; left: 0; width: 100%; text-align: center;
    font-size: 20px; font-weight: 400; line-height: 1; color: var(--ink);
  }
  .product-grid { position: absolute; inset: 0; }
  .frame-label { font-family: "Tinos", "Times New Roman", serif; font-size: 7px; fill: var(--ink); }
</style>
</head>
<body>
<div class="canvas">
  <svg class="crop-marks" width="1200" height="880" viewBox="0 0 1200 880" aria-hidden="true">
    <g stroke="var(--crop-black)" stroke-width="1.4">
      <line x1="20" y1="43" x2="35" y2="43"/><line x1="40" y1="24" x2="40" y2="38"/>
      <line x1="1165" y1="43" x2="1180" y2="43"/><line x1="1160" y1="24" x2="1160" y2="38"/>
      <line x1="20" y1="836" x2="35" y2="836"/><line x1="40" y1="841" x2="40" y2="856"/>
      <line x1="1165" y1="836" x2="1180" y2="836"/><line x1="1160" y1="841" x2="1160" y2="856"/>
    </g>
  </svg>

  <div class="page">
    <div class="leaves-top" role="img" aria-label="Scattered pink maple leaves along the top edge"></div>
    <div class="leaves-bottom left" role="img" aria-label="Scattered pink leaves, bottom left corner"></div>
    <div class="leaves-bottom centre" role="img" aria-label="Scattered pink leaves, bottom centre"></div>
    <div class="leaves-bottom right" role="img" aria-label="Scattered pink leaves, bottom right corner"></div>

    <svg class="product-grid" width="1107" height="777" viewBox="0 0 1107 777" aria-label="Product frames">
      <defs>
        <g id="product-frame">
          <rect x="0.5" y="0.5" width="52" height="78" fill="none" stroke="var(--frame-grey)" stroke-width="1"/>
          <line x1="0.5" y1="66.2" x2="52.5" y2="66.2" stroke="var(--frame-grey)" stroke-width="1"/>
          <text class="frame-label" x="26.5" y="75.6" text-anchor="middle">TEXT</text>
        </g>
        <g id="frame-row">
          <use href="#product-frame" x="0"/>
          <use href="#product-frame" x="66.6"/>
          <use href="#product-frame" x="133.2"/>
          <use href="#product-frame" x="199.8"/>
          <use href="#product-frame" x="266.4"/>
          <use href="#product-frame" x="333"/>
          <use href="#product-frame" x="399.6"/>
          <use href="#product-frame" x="466.2"/>
        </g>
        <g id="frame-grid">
          <use href="#frame-row" y="0"/>
          <use href="#frame-row" y="92.4"/>
          <use href="#frame-row" y="184.8"/>
          <use href="#frame-row" y="277.2"/>
          <use href="#frame-row" y="369.6"/>
          <use href="#frame-row" y="462"/>
          <use href="#frame-row" y="554.4"/>
        </g>
      </defs>
      <use href="#frame-grid" x="14.5" y="108.5"/>
      <use href="#frame-grid" x="572.5" y="108.5"/>
    </svg>

    <section class="spread-half left">
      <h1 class="brand-title">Vitrel</h1>
      <h2 class="section-heading">Text Box</h2>
      <p class="website">Website Address</p>
    </section>
    <section class="spread-half right">
      <h1 class="brand-title">Vitrel</h1>
      <h2 class="section-heading">Text Box</h2>
      <p class="website">Website Address</p>
    </section>
  </div>
</div>
</body>
</html>
```